Tallgrove Vale Management

I need a professional website. My current website is tallgrovevalemanagement.com and I hate it. It was created with some AI tool very quickly because I needed a site up and running with no advanced notice. I’m open to all designs .. I trust you, the professionals will deliver the results I’m anxiously awaiting! :)

```html
<!DOCTYPE html>
<html lang="en">
<head>
<meta charset="utf-8">
<title>Tallgrove Vale Management</title>
<link href="https://fonts.googleapis.com/css2?family=Poppins:wght@300;400;500;600;700;800&display=swap" rel="stylesheet">
<style>
:root{
  --navy:#22335a;
  --red:#d0282e;
  --ink:#111111;
  --white:#ffffff;
  --grey:#f3f4f6;
  --sky:#c9dcef;
  --text:#2b2b2b;
}
*{box-sizing:border-box;margin:0;padding:0}
html,body{width:1200px;height:3382px;overflow:hidden}
body{position:relative;font-family:"Poppins",sans-serif;color:var(--text);background:var(--white)}
.abs{position:absolute}
/* top bar */
.topbar{left:420px;top:0;width:780px;height:39px;background:var(--navy);clip-path:polygon(0 0,100% 0,100% 100%,22px 100%)}
.topbar .email{position:absolute;left:52px;top:12px;font-size:10px;color:var(--white);letter-spacing:.2px}
.topbar .social{position:absolute;right:112px;top:12px;font-size:10px;color:var(--white)}
.dots{display:inline-flex;gap:14px;margin-left:14px;vertical-align:middle}
.dots i{width:7px;height:7px;border-radius:50%;background:currentColor;display:block}
.header{left:0;top:39px;width:1200px;height:61px;background:var(--white)}
.brandbox{left:131px;top:0;width:125px;height:148px;background:var(--white);box-shadow:0 4px 14px rgba(0,0,0,.18);z-index:5;display:flex;align-items:center;justify-content:center;text-align:center;clip-path:polygon(0 0,100% 0,100% 85%,50% 100%,0 85%)}
.brandbox span{font-weight:800;font-size:15px;line-height:1.15;color:var(--navy)}
.nav{left:422px;top:62px;display:flex;gap:34px;font-size:10px;color:#333}
.quote{left:944px;top:50px;width:125px;height:39px;background:var(--red);color:var(--white);font-size:10px;font-weight:600;display:flex;align-items:center;justify-content:center;clip-path:polygon(14px 0,100% 0,100% 100%,14px 100%,0 50%)}
/* hero */
.hero-photo{left:0;top:100px;width:1200px;height:745px;background:linear-gradient(180deg,#6d7378 0%,#8c939a 35%,#c9c6c0 60%,#5b5a55 85%,#3c3d3a 100%)}
.hero-shade{left:0;top:100px;width:1200px;height:300px;background:linear-gradient(180deg,rgba(70,72,76,.45),rgba(70,72,76,0))}
.hero-cut{left:0;top:700px;width:1200px;height:160px}
.hero-tag{left:0;top:215px;width:1200px;text-align:center;font-size:10px;color:var(--white);letter-spacing:.3px}
.hero-tag b{font-weight:400;display:inline-block;padding:0 12px}
.hero-tag .ln{display:inline-block;width:55px;height:1px;background:var(--white);vertical-align:middle}
.hero-title{left:0;top:240px;width:1200px;text-align:center;font-weight:800;font-size:58px;line-height:1.1;color:var(--white);letter-spacing:-.5px}
.hero-title em{font-style:normal;color:var(--red)}
/* about */
.hex{left:131px;top:936px;width:469px;height:492px;clip-path:polygon(50% 0,7% 27%,7% 46%,0 46%,0 65%,7% 65%,7% 81%,50% 100%,93% 81%,93% 65%,100% 65%,100% 46%,93% 46%,93% 27%);background:linear-gradient(180deg,#9cc4ea 0%,#d9e6f2 30%,#ece9e2 55%,#7f8f6b 85%,#5c6a47 100%)}
.label{font-size:10px;color:var(--red);display:flex;align-items:center;gap:8px}
.label .ln{width:55px;height:1px;background:var(--red)}
.h2{font-weight:800;font-size:33px;line-height:1.12;color:var(--ink);text-transform:uppercase}
.h2 em{font-style:normal;color:var(--red)}
.body{font-size:10.5px;line-height:1.5;color:#333;font-weight:300}
.btn-red{background:var(--red);color:var(--white);font-size:10px;font-weight:600;display:flex;align-items:center;justify-content:center;clip-path:polygon(14px 0,100% 0,100% 100%,14px 100%,0 50%)}
/* services */
.services{left:0;top:1520px;width:1200px;height:736px;background:var(--grey)}
.card{top:1772px;width:272px;height:376px;overflow:hidden}
.card .photo{position:absolute;inset:0}
.card .cap{position:absolute;left:0;right:0;bottom:0;height:110px;background:linear-gradient(180deg,rgba(0,0,0,0),rgba(0,0,0,.95));color:var(--white);font-weight:700;font-size:15px;display:flex;align-items:flex-end;justify-content:center;padding-bottom:26px;text-transform:uppercase}
.card.feature{background:linear-gradient(180deg,#d86663 0%,#cf5552 70%,#8a1a1e 100%);color:var(--white);text-align:center}
.card.feature .mark{position:absolute;left:86px;top:60px;width:100px;font-weight:800;font-size:11px;line-height:1.2;color:var(--white)}
.card.feature h3{position:absolute;left:0;right:0;top:150px;font-size:15px;font-weight:700}
.card.feature .price{position:absolute;left:0;right:0;top:172px;font-size:20px;font-weight:700}
.card.feature p{position:absolute;left:22px;right:22px;top:200px;font-size:10.5px;line-height:1.5;font-weight:300}
.card.feature .cart{position:absolute;left:66px;top:280px;width:123px;height:36px;background:var(--white);color:var(--ink);font-size:10px;font-weight:600;display:flex;align-items:center;justify-content:center;clip-path:polygon(14px 0,100% 0,100% 100%,14px 100%,0 50%)}
/* contact */
.contact-bg{left:0;top:2256px;width:1200px;height:900px;background:linear-gradient(180deg,#c4d9ef 0%,#d3e3f3 60%,#e6eef7 100%)}
.contact-photo{left:0;top:2760px;width:1200px;height:420px;background:linear-gradient(180deg,rgba(210,225,240,0) 0%,#8b97a3 30%,#c8ccd0 55%,#4c5a45 85%,#3f4a3a 100%)}
.form{left:168px;top:2349px;width:865px;height:448px;background:var(--navy);color:var(--white)}
.form .label{position:absolute;left:0;right:0;top:44px;justify-content:center}
.form h2{position:absolute;left:0;right:0;top:60px;text-align:center;font-weight:800;font-size:33px;text-transform:uppercase}
.form .sub{position:absolute;left:0;right:0;top:107px;text-align:center;font-size:10.5px;font-weight:300}
.field{position:absolute;background:var(--white);color:#333;font-size:10.5px;padding:12px 16px}
.send{position:absolute;left:26px;top:357px;width:818px;height:38px;background:var(--red);font-size:9.5px;font-weight:600;display:flex;align-items:center;justify-content:center}
.send svg{position:absolute;right:24px;top:14px}
/* footer */
.footer-shape{left:0;top:3070px;width:1200px;height:312px}
.foot-brand{left:131px;top:3210px;width:145px;height:140px;display:flex;align-items:center;justify-content:center;text-align:center;font-weight:800;font-size:17px;line-height:1.15;color:var(--white)}
.foot-nav{left:422px;top:3267px;display:flex;gap:42px;font-size:10px;font-weight:600;color:var(--white)}
.foot-rule{left:422px;top:3306px;width:647px;height:1px;background:rgba(255,255,255,.25)}
.copy{left:422px;top:3325px;font-size:9.5px;color:var(--white)}
.foot-social{left:905px;top:3327px;font-size:9.5px;font-weight:600;color:var(--white)}
</style>
</head>
<body>

<div class="abs topbar">
  <div class="email">&#9993;&nbsp; INFO@TALLGROVEVALEMANAGEMENT.COM</div>
  <div class="social">Social Media: <span class="dots"><i></i><i></i><i></i><i></i></span></div>
</div>
<div class="abs header"></div>
<div class="abs brandbox"><span>TALLGROVE<br>VALE<br>MANAGEMENT</span></div>
<nav class="abs nav"><span>HOME</span><span>OUR SERVICES</span><span>ABOUT US</span><span>TESTIMONIALS</span><span>GALLERY</span><span>CONTACT US</span></nav>
<div class="abs quote">REQUEST A QUOTE</div>

<section>
  <div class="abs hero-photo" role="img" aria-label="Modern white house with dark roof and warm lit windows among trees"></div>
  <div class="abs hero-shade"></div>
  <svg class="abs hero-cut" width="1200" height="160" viewBox="0 0 1200 160">
    <polygon points="0,113 330,86 1200,35 1200,160 0,160" fill="#ffffff"/>
    <polygon points="320,88 748,55 1200,35 1200,60 350,116" fill="#e3ece9"/>
    <polygon points="748,55 1200,20 1200,143" fill="#d0282e"/>
  </svg>
  <div class="abs hero-tag"><span class="ln"></span><b>CLEVELAND - AKRON · PROPERTY MANAGEMENT</b><span class="ln"></span></div>
  <h1 class="abs hero-title">A TRUE PARTNER,<br>NOT JUST A <em>VENDOR.</em></h1>
</section>

<section>
  <div class="abs hex" role="img" aria-label="White villa with balconies and palm trees under blue sky"></div>
  <div class="abs label" style="left:649px;top:989px"><span class="ln"></span>ABOUT US</div>
  <h2 class="abs h2" style="left:649px;top:1012px">About our property<br><em>management</em> solutions</h2>
  <p class="abs body" style="left:649px;top:1103px;width:400px">Our organization delivers comprehensive property management solutions that optimize asset performance and tenant satisfaction. By integrating advanced analytics with proven operational frameworks, our specialists ensure each property achieves sustained value appreciation.</p>
  <p class="abs body" style="left:649px;top:1181px;width:400px">Drawing on decades of collective expertise, the team facilitates regulatory compliance, cost efficiency, and proactive maintenance. This disciplined approach enables owners to preserve capital, enhance occupancy rates, and demonstrate long-term resilience across diverse market conditions.</p>
  <div class="abs btn-red" style="left:651px;top:1272px;width:125px;height:38px">READ MORE</div>
</section>

<section>
  <div class="abs services"></div>
  <div class="abs label" style="left:131px;top:1602px"><span class="ln"></span>OUR SERVICES</div>
  <h2 class="abs h2" style="left:131px;top:1636px">Strategic property<br><em>management</em> solutions</h2>
  <p class="abs body" style="left:600px;top:1603px;width:470px">Our analysis demonstrates that effective property oversight originates from meticulous operational planning, transparent communication channels, and data-driven performance metrics across every asset class.</p>
  <p class="abs body" style="left:600px;top:1666px;width:470px">By integrating advanced technology with industry expertise, our team implements proactive maintenance schedules that preserve asset value and facilitate sustainable, long-term returns for stakeholders.</p>

  <div class="abs card" style="left:131px">
    <div class="photo" role="img" aria-label="Hands comparing fabric samples on a wooden table" style="background:linear-gradient(160deg,#8a6c4f 0%,#c9a77f 45%,#e2d3bd 70%,#b69672 100%)"></div>
    <div class="cap">Basic Service</div>
  </div>
  <div class="abs card feature" style="left:416px">
    <div class="mark">TALLGROVE VALE MANAGEMENT</div>
    <h3>INTERMEDIATE SERVICE</h3>
    <div class="price">$99.00</div>
    <p>Describe important details like price, value, length of service, and why it's unique. Or use these sections to showcase different key values of your products or services.</p>
    <div class="cart">ADD TO CART</div>
  </div>
  <div class="abs card" style="left:701px">
    <div class="photo" role="img" aria-label="Desk with white lilies in a vase and a small lamp" style="background:linear-gradient(160deg,#7c6a55 0%,#d9cfc2 40%,#c8b39b 65%,#8c7a66 100%)"></div>
    <div class="cap">Advanced Service</div>
  </div>
  <div class="abs card" style="left:986px;width:214px">
    <div class="photo" role="img" aria-label="Hand flipping through material swatches" style="background:linear-gradient(160deg,#c8b49a 0%,#e0d2bf 45%,#9a8168 75%,#5e4b3a 100%)"></div>
    <div class="cap" style="justify-content:flex-start;padding-left:57px;white-space:nowrap">Advanced Service</div>
  </div>
</section>

<section>
  <div class="abs contact-bg"></div>
  <div class="abs contact-photo" role="img" aria-label="Modern white house with dark roof surrounded by trees"></div>
  <div class="abs form">
    <div class="label"><span class="ln"></span>CONTACT US<span class="ln"></span></div>
    <h2>Request a tailored proposal</h2>
    <div class="sub">Submit the form to initiate a consultative assessment and explore solutions aligned with your objectives.</div>
    <div class="field" style="left:26px;top:136px;width:405px;height:41px">First Name</div>
    <div class="field" style="left:440px;top:136px;width:404px;height:41px">Last Name</div>
    <div class="field" style="left:26px;top:186px;width:405px;height:41px">Phone No</div>
    <div class="field" style="left:440px;top:186px;width:404px;height:41px">Email Address</div>
    <div class="field" style="left:26px;top:235px;width:818px;height:114px">Message (required)</div>
    <div class="send">SEND NOW
      <svg width="10" height="10" viewBox="0 0 10 10"><path d="M0 4.5 10 0 6 10 4.6 5.4Z" fill="#fff"/></svg>
    </div>
  </div>
</section>

<footer>
  <svg class="abs footer-shape" width="1200" height="312" viewBox="0 0 1200 312">
    <polygon points="0,70 1200,40 1200,312 0,312" fill="#050505"/>
    <polygon points="760,125 1200,10 1200,80" fill="#d0282e"/>
  </svg>
  <div class="abs foot-brand">TALLGROVE<br>VALE<br>MANAGEMENT</div>
  <nav class="abs foot-nav"><span>HOME</span><span>OUR SERVICES</span><span>ABOUT US</span><span>TESTIMONIALS</span><span>GALLERY</span><span>CONTACT US</span></nav>
  <div class="abs foot-rule"></div>
  <div class="abs copy">COPYRIGHT 2026.TALLGROVE VALE MANAGEMENT. ALL RIGHT RESERVED</div>
  <div class="abs foot-social">SOCIAL MEDIA: <span class="dots"><i></i><i></i><i></i><i></i></span></div>
</footer>

</body>
</html>
```